Industrial Consulting Firm Looking for a Responsive Design

Looking for a responsive design website of around 5 parent pages and about another 15 sub-pages for a small firm that works globally at industrial construction sites.

The web address http://torvexmilan.com/brightlo482917/index.html includes most of the content we would like to use for this effort. There are two deliverable options:

1) Use the provided design and create graphics for the website along with other requested tweaks.
2) Create a entirely new Layout/Design, which is original and different from this example, using content (text) from the provided link.

Content:

The main components of the website should include graphics for main page headers and picture links (along with the 7 main service sub pages), with industrial themes for the following pages:

Landing Page with clean presentation of our company and services.

Services: This main page has the most important sub-links in the website, the services which we want to highlight (Statistical Productivity Improvement, Veradin Process, Improving Project Performance, Work Process Analysis & Mapping, On-Site Training, and Facilitation Support). We would like to see graphic headers for each of these pages. Would like to have a fact sheet template.

News & Insight (Blog/Content Delivery format for press releases, latest news, publications, ability to be linked to company facebook feed a plus, etc)

Information about the company (Mission, Description, Company Profile, Clients Served,FAQs). Also, an interactive world map of past projects with capacity to update. It should work by obtaining a detail summary of past projects by hovering/clicking locations.

Contact Form including link to careers

Feel free to update any tables or content in pages. Ideas to highlight our services through graphics are appreciated.

Optional Features To Consider:

Client Testimonial Section (possibly on Main Page or About Us)
Filtering of News by Category/Date
Basic Site Search Functionality
Add a Registration option for Site Updates

Other Details:

If using pictures with people wearing safety gear: make sure that they are wearing safety glasses and a hard hat at a minimum and that the picture looks as realistic (environment-wise) as possible
Guidance on inclusion of other company logos in websites (as clients references, or displayed in pictures). Potentially looking to include them in website (either on landing page or clients served section in about us).

Important Considerations:

The design should be mobile (Android, IOS) friendly (NOT a separate mobile site)
The design should incorporate SEO.
The design should take security into account.
Coding required as well as graphic template files.

Upcoming Project Opportunity

Based on the demonstrated graphic design presented in this project, we might consider an additional project to expand on graphics package (including, but not limited to an info graphic).

Technical Requirements:

Languages Accepted: HTML, ASP.NET
To Run on a Server with: Windows IIS 7 or above
Restrictions: No languages requiring install on Windows IIS
Easily updated and maintained

Project will commit payment when we find at least one design our team agrees upon.

```html
<!DOCTYPE html>
<html lang="en">
<head>
<meta charset="utf-8">
<title>Stridewell Output Partners</title>
<link href="https://fonts.googleapis.com/css2?family=Raleway:ital,wght@0,400;0,500;0,600;0,700;0,800;1,400;1,700&display=swap" rel="stylesheet">
<style>
:root{
  --navy:#0b2a55;
  --navy-deep:#071d3d;
  --blue:#0f4a93;
  --brown:#8a6a55;
  --brown-dark:#5b4536;
  --ink:#3a3a3a;
  --muted:#777;
  --paper:#f1efec;
  --line:#d8d4cf;
  --white:#fff;
}
*{box-sizing:border-box;margin:0;padding:0}
html,body{width:1200px;height:3249px;overflow:hidden}
body{font-family:'Raleway',sans-serif;color:var(--ink);background:#fff;font-size:13px}
.wrap{width:720px;margin:0 auto;position:relative}
a{color:inherit;text-decoration:none}

/* header */
.topbar{height:58px;background:#fff;position:relative;z-index:3}
.topbar .wrap{display:flex;align-items:center;height:58px}
.brand{display:flex;align-items:center;gap:10px;font-weight:700;font-size:13px;letter-spacing:1px;color:var(--navy);line-height:1.15;width:240px}
.brand .dot{width:40px;height:40px;border-radius:50%;background:var(--navy);flex:none}
.contact-bits{display:flex;gap:26px;margin-left:40px;font-size:11px;color:var(--ink);line-height:1.35}
.contact-bits div{display:flex;align-items:center;gap:8px}
.social{display:flex;gap:6px;margin-left:auto}
.social span{width:22px;height:22px;border-radius:50%;background:var(--navy)}
.social span:nth-child(2),.social span:nth-child(3),.social span:nth-child(4){background:var(--brown)}
.nav{position:absolute;top:58px;left:277px;width:643px;height:46px;background:var(--navy);z-index:3;display:flex;align-items:center;padding:0 22px;gap:26px;color:#fff;font-size:11px;font-weight:500;letter-spacing:.5px}
.nav .sep{margin-left:auto;display:flex;gap:18px;color:#9fb3cf}

/* hero */
.hero{position:relative;height:498px;margin-top:24px;background:radial-gradient(ellipse at 50% 60%,#4a5f83 0%,#2b3c5c 45%,#141f36 100%);color:#fff;text-align:center}
.hero-art{position:absolute;inset:0}
.hero-copy{position:relative;padding-top:62px}
.hero h1{font-weight:400;font-size:21px}
.hero h1 em{font-weight:700}
.hero p{width:470px;margin:18px auto 0;font-size:13px;line-height:1.45;color:#dfe6f1}
.btn-ghost{display:inline-block;margin-top:22px;border:1px solid #fff;padding:7px 16px;font-size:11px;letter-spacing:1px}

/* welcome */
.welcome{height:293px;background:#fff}
.welcome .wrap{display:flex;height:293px;width:730px}
.welcome-photo{width:330px;height:293px;background:linear-gradient(135deg,#c9ccd1,#8e969f 60%,#5d6670);clip-path:polygon(0 0,100% 0,85% 100%,0 100%)}
.welcome-copy{padding:40px 0 0 10px;width:390px}
.kicker{color:var(--brown);font-size:11px;letter-spacing:1px}
.welcome h2{color:var(--navy);font-size:17px;font-weight:800;line-height:1.15;margin-bottom:14px}
.welcome p{font-size:10.5px;line-height:1.45;margin-bottom:9px}
.btn-row{display:flex;gap:8px;margin-top:12px}
.btn-line{border:1px solid var(--navy);padding:7px 12px;font-size:10.5px;color:var(--navy)}
.btn-line b{font-weight:800}

/* mission */
.mission{height:204px;background:linear-gradient(180deg,#0d3f82,#0a2f63);color:#fff;text-align:center;padding-top:36px}
.mission h2{font-size:18px;font-weight:800}
.rule{width:40px;height:2px;background:#4fb2e6;margin:8px auto 14px}
.mission p{width:480px;margin:0 auto;font-style:italic;font-size:17px;line-height:1.3;color:#b9cbe6}

/* services */
.services{height:476px;background:linear-gradient(180deg,#ececec,#dadada)}
.services-head{text-align:center;padding-top:30px}
.services h2{color:var(--navy);font-size:17px;font-weight:800}
.services .sub{font-size:10px;letter-spacing:1px;color:var(--muted);margin-top:4px}
.tabs{display:flex;width:716px;margin:18px auto 0;height:104px}
.tab{flex:1;background:linear-gradient(180deg,#fff,#dcdcdc);border-right:1px solid var(--line);padding:20px 8px 0 10px;font-size:14px;line-height:1.15;color:var(--ink)}
.tab.active{background:var(--brown);color:#fff;height:104px;position:relative}
.tab.active:after{content:"";position:absolute;left:50%;bottom:-10px;margin-left:-10px;border:10px solid transparent;border-bottom:0;border-top-color:var(--brown)}
.svc{display:flex;width:716px;margin:14px auto 0;gap:14px}
.svc-copy{width:376px}
.svc h3{color:var(--navy);font-size:17px;font-weight:800;margin:6px 0 6px}
.svc p{font-size:9.5px;line-height:1.4;margin-bottom:7px}
.svc .more{font-size:10px;color:var(--brown)}
.svc-photo{width:326px;height:192px;background:linear-gradient(135deg,#eaeaea,#bfc3c8 55%,#8d9298)}

/* news */
.news{height:403px;background:var(--paper);text-align:center;padding-top:38px}
.news h2,.clients h2{color:var(--navy);font-size:17px;font-weight:800}
.news-grid{display:grid;grid-template-columns:1fr 1fr;width:716px;margin:18px auto 0;column-gap:40px;row-gap:24px;text-align:left}
.item{display:flex;gap:12px}
.date{width:92px;text-align:right;flex:none;color:var(--ink)}
.date b{display:block;font-size:34px;font-weight:400;line-height:1}
.date small{font-size:9px}
.item p{font-size:9.5px;line-height:1.4}
.item a{display:block;margin-top:10px;font-size:9.5px;color:var(--brown)}
.btn-news{display:inline-block;margin-top:30px;border:1px solid var(--navy);padding:8px 24px;font-size:11px;color:var(--navy)}

/* newsletter */
.newsletter{height:189px;background:linear-gradient(90deg,#3f3127,#6e5646 50%,#3f3127);color:#fff;text-align:center;padding-top:60px}
.newsletter h2{font-weight:400;font-size:19px}
.newsletter span{display:inline-block;margin-top:14px;border:1px solid #d9cbbd;padding:6px 18px;font-size:11px}

/* testimonials */
.clients{height:342px;background:#fff;text-align:center;padding-top:36px}
.quotes{display:flex;gap:16px;width:716px;margin:18px auto 0}
.quote{flex:1;border:1px solid #9fb0c4;padding:18px 14px;height:206px;font-size:9px;line-height:1.45}
.quote.mid{margin-top:-10px;height:216px}
.quote .name{font-style:italic;color:var(--brown);font-size:14px}
.quote .role{font-weight:700;font-size:10px;margin:3px 0 10px;color:var(--ink)}
.pager{margin-top:14px;display:flex;justify-content:center;gap:4px}
.pager i{width:5px;height:5px;border-radius:50%;background:#999}
.pager i:first-child{background:var(--navy)}

/* contact */
.contact{height:411px;background:radial-gradient(ellipse at 50% 20%,#174c8e,#0a2c5e 60%,#061c3e);color:#fff;text-align:center;padding-top:62px}
.contact h2{font-size:17px;font-weight:800}
.contact p{width:480px;margin:0 auto;font-size:10.5px;line-height:1.45;color:#d7e1ef}
.form{width:480px;margin:40px auto 0;text-align:left;font-size:10px}
.row{display:flex;gap:30px}
.field{flex:1;border-bottom:1px solid #cfd9e7;padding-bottom:8px;margin-bottom:52px;color:#d7e1ef}
.send{display:block;margin:-26px 0 0 auto;width:104px;border:1px solid #cfd9e7;padding:6px 0;text-align:center;font-size:10px}

/* map */
.map{height:282px;background:linear-gradient(180deg,#ece7db,#e2dccd);position:relative}
.social-big{position:absolute;left:50%;top:258px;transform:translateX(-50%);display:flex;gap:10px;z-index:2}
.social-big span{width:48px;height:48px;border-radius:50%;background:var(--navy)}

/* footer */
.footer{height:69px;background:#111;color:#ccc;font-size:9px}
.footer .wrap{display:flex;justify-content:space-between;padding-top:30px;width:700px;line-height:1.3}
</style>
</head>
<body>

<header class="topbar">
  <div class="wrap">
    <a class="brand" href="#"><span class="dot"></span>STRIDEWELL OUTPUT<br>PARTNERS</a>
    <div class="contact-bits">
      <div><svg width="18" height="18" viewBox="0 0 24 24"><path d="M6 2l4 4-2 3c1 3 4 6 7 7l3-2 4 4-3 4C10 22 2 14 2 5z" fill="#333"/></svg>(555) 014-2270<br>hello@stridewelloutput.com</div>
      <div><svg width="20" height="18" viewBox="0 0 24 22"><path d="M12 1L1 11h3v10h6v-6h4v6h6V11h3z" fill="#333"/></svg>P.O. Box 118<br>Larkfield, NC 20000</div>
    </div>
    <div class="social"><span></span><span></span><span></span><span></span></div>
  </div>
</header>
<nav class="nav">
  <a>HOME</a><a>SERVICES ▾</a><a>NEWS &amp; INSIGHTS ▾</a><a>ABOUT US ▾</a><a>CONTACT ▾</a>
  <div class="sep"><a>LOGIN</a><a>SEARCH</a></div>
</nav>

<section class="hero">
  <div class="hero-art" role="img" aria-label="Two business people in suits shaking hands over a blue world map"></div>
  <div class="hero-copy">
    <h1>Partnering with clients to <em>improve</em> productivity.</h1>
    <p>We have over 20 years of performance improvement experience in the engineering and construction industry and can design a productivity improvement solution specific to your needs</p>
    <a class="btn-ghost">START <b>TOUR</b></a>
  </div>
</section>

<section class="welcome">
  <div class="wrap">
    <div class="welcome-photo" role="img" aria-label="Engineers in hard hats and safety glasses reviewing a site"></div>
    <div class="welcome-copy">
      <div class="kicker">WELCOME TO</div>
      <h2>STRIDEWELL OUTPUT<br>PARTNERS</h2>
      <p>Stridewell Output Partners (SOP) is a performance improvement firm specializing in providing improvement services for the engineering and construction industry.</p>
      <p>SOP utilizes award-winning industry "Best Practice" measurement techniques, combined with proven Lean Construction and Total Quality Management concepts to drive improvement of project execution performance and ultimately help clients increase their bottom lines.</p>
      <div class="btn-row"><a class="btn-line">VIEW OUR <b>SERVICES</b></a><a class="btn-line">DOWNLOAD <b>PDF SHEET</b></a></div>
    </div>
  </div>
</section>

<section class="mission">
  <h2>OUR MISSION</h2>
  <div class="rule"></div>
  <p>To assist clients in creating more productive work processes by applying our tools, technology, expertise and support specific to each client's unique opportunities.</p>
</section>

<section class="services">
  <div class="services-head">
    <h2>OUR SERVICES</h2>
    <div class="sub">"SOFTER" SERVICES LIKE FACILITATION AND TRAINING</div>
  </div>
  <div class="tabs">
    <div class="tab">Statistical Productivity Improvement</div>
    <div class="tab">Veradin Process</div>
    <div class="tab">Improving Project Performance</div>
    <div class="tab active">Work Process Analysis &amp; Mapping</div>
    <div class="tab">On-Site Training</div>
    <div class="tab">Facilitation Support</div>
  </div>
  <div class="svc">
    <div class="svc-copy">
      <h3>WORK PROCESS ANALYSIS &amp; MAPPING</h3>
      <p>Work Process Analysis &amp; Mapping is a methodical deconstruction of core work processes to identify constraints directly affecting construction execution. Building on alignment and Key Performance Indicators at each control juncture throughout the project organization, SOP works closely with key personnel to verify actual versus target process execution, and understand sources of systematic variability that erode effective workface construction execution. A detailed cross-functional process map is created, with constraints and proposed KPIs identified throughout, which indicate the most significant opportunities for improvement.</p>
      <p>Working with stakeholders, processes are realigned to mirror project strategy. KPIs are refined for implementation to control variability and improve predictability, which are key to enabling improvements in construction efficiency and productivity. Reducing constraints in upstream processes can impact mid-stream and end-of-stream outcomes, as well as benefit future phases of construction.</p>
      <a class="more">Read More</a>
    </div>
    <div class="svc-photo" role="img" aria-label="Team gathered around a table with tablets and documents"></div>
  </div>
</section>

<section class="news">
  <h2>LATEST NEWS</h2>
  <div class="rule"></div>
  <div class="news-grid">
    <div class="item"><div class="date"><b>25</b><small>January 2014</small></div><div><p>Stridewell Output Partners (SOP) announced today the award of a Productivity Consulting Services contract. SOP will be serving the Costa Vela Refinery Expansion Project in Cartagena, Colombia (South America). The client is Costa Vela Refinery.</p><a>Read More</a></div></div>
    <div class="item"><div class="date"><b>03</b><small>January 2014</small></div><div><p>SOP will be serving the Costa Vela Refinery Expansion Project in Cartagena, Colombia (South America). The client is Costa Vela Refinery.</p><a>Read More</a></div></div>
    <div class="item"><div class="date"><b>17</b><small>January 2014</small></div><div><p>Productivity Consulting Services contract. SOP will be serving the Costa Vela Refinery Expansion Project in Cartagena, Colombia (South America). The client is Costa Vela Refinery.</p><a>Read More</a></div></div>
    <div class="item"><div class="date"><b>26</b><small>December 2013</small></div><div><p>Announced today the award of a Productivity Consulting Services contract. SOP will be serving the Costa Vela Refinery Expansion Project in Cartagena, Colombia (South America). The client is Costa Vela Refinery.</p><a>Read More</a></div></div>
  </div>
  <a class="btn-news">VIEW ALL <b>NEWS</b></a>
</section>

<section class="newsletter" role="img" aria-label="Construction workers in hard hats on an industrial site, in sepia tones">
  <h2>Want to hear more story, Subscribe for our newsletter</h2>
  <span>Subscribe</span>
</section>

<section class="clients">
  <h2>WHAT CLIENTS SAY...</h2>
  <div class="rule"></div>
  <div class="quotes">
    <div class="quote"><div class="name">Mara Quill</div><div class="role">Supervisor</div><p>SOP has partnered with clients on their most critical projects around the world. Some of these companies include: Harlan Petroleum, Northgate Energy, Brisk Power, Calder Oil and Westmoor Marine.</p><p><br>Delta Valley Authority, Arcwell Builders, Tessan Group, Ridgeway and the Prairie Trades Council.</p></div>
    <div class="quote mid"><div class="name">Mara Quill</div><div class="role">General Manager</div><p>SOP has provided improvement services to many industry leading engineering and construction companies and facility owners all around the world. SOP services have been implemented successfully across a broad spectrum of industry sectors including Oil &amp; Gas, Mining, Utilities (fossil, hydro and nuclear), Chemical Products, Refinery Products, Industrial fabrication for both onshore and offshore facilities and many more.</p></div>
    <div class="quote"><div class="name">Mara Quill</div><div class="role">IT Manager</div><p>Some of the subcontractors SOP has collaborated with include: Orrin Builders, Pasco Lane, Tessan Group, Holtby Works, Marlin Civil, Quarry Point, Kestrel, Ardent, Fennick, Lowden, Saberin and Vantor.</p></div>
  </div>
  <div class="pager"><i></i><i></i><i></i><i></i><i></i></div>
</section>

<section class="contact" role="img" aria-label="Deep blue world map backdrop">
  <h2>CONTACT US</h2>
  <div class="rule"></div>
  <p>If you would like to schedule a call or a business meeting to learn more about our company or services, please complete the following form below. We will get in touch with you as soon as possible.</p>
  <div class="form">
    <div class="row"><div class="field">Yor name here</div><div class="field">Yor mail here</div></div>
    <div class="field">Yor message here</div>
    <a class="send">Send Message</a>
  </div>
</section>

<section class="map" role="img" aria-label="Road map of the southern United States marking past project locations">
  <div class="social-big"><span></span><span></span><span></span><span></span></div>
</section>

<footer class="footer">
  <div class="wrap">
    <div>© 2015 - STRIDEWELL OUTPUT PARTNERS, Inc.<br>All Right Reserved</div>
  </div>
</footer>

</body>
</html>
```